Electric Skateboard Website - California Beach - Psychedelic - Graffiti Style

CARTVANE WEBSITE: Opening a online electric skateboard shop. We'll ultimately sell Electric Skateboards, Scooters and Bikes. I opened a Cartvane account and even purchased a domain. But, after 3 weeks of trying, I realize, my skills are inadequate. I'd love to have a cool website that links to Parcelbay / Bidlot / Snapreel / Friendwall etc.I'd really like to emphasize that we're a coastal california company, with offices in Hermosa Beach, Venice Beach, and Santa Cruz. I like the colorful, psychedelic color patterns, with graffiti letteringIdeally, I'd like to have a couple pages1. Landing Page with a menu for2. Electric Skateboards (a) Street skateboards (small wheels) (4 offerings) (b) Commuter / offroad skateboards (2 offerings)2. Scooter (1 offering)3. Bikes (1 offering)4. Parts5. Link to an apparel site6. Blog / Safety Tips / Maintenance7. Our Company?I've attached a couple pix and logos etc. I suspect you'll see I have an idea of what I want to do, but my execution isn't so good...I love to have some input and for somebody to help me get a site running! THANK YOU!!

Target Market(s)

Not entirely sure. My gut is 20 - 40 year olds, largely male. Commuters and Students

Industry/Entity Type

Sporting Good

Contact Information for Business Card

I really like the Graffiti Style lettering, you'll see I did them poorly on the attachment - originally, I thought that some bright, graffiti lettering of Q&Q Electric Skateboards or Tidewave Skateboards on the front. Bright logo on the back with all of the information below
Marco Penhale
(213) 555-0147
mpenhale@qqboardworks.example
www.qqboardworks.example

Coding

Coded - Design and coding required

Number of Pages Required

1 page

Font styles to use
Other font styles liked:
• Comic Sans MS

Colors
fbed22
e34197
ec1f27
0292cd
6b449b

Requirements
Must have
• Please See "Final Design Selection" (one of the last files on my upload list) to get a sense of the custom decks we're having printed. These are the first couple, but, I think you'll get a sense
• Also, please look at the "Logo - First Attempt " powerpoint file. That's my attempt at graffiti style lettering (one of the last files on the list of uploads)
• Finally, please look at the Delia Markovetz photo (first file on upload list). It's a public access photo. But, I love the picture

```html
<!DOCTYPE html>
<html lang="en">
<head>
<meta charset="utf-8">
<title>Tidewave Skateboards — Electric Skateboards, Scooters &amp; Bikes</title>
<link href="https://fonts.googleapis.com/css2?family=Kalam:wght@400;700&family=Lato:wght@400;700&family=Poppins:wght@500;600&display=swap" rel="stylesheet">
<style>
:root{
  --red:#ec1f27;
  --yellow:#fbed22;
  --pink:#e34197;
  --blue:#0292cd;
  --purple:#6b449b;
  --ink:#222;
  --body:#555;
  --muted:#888;
  --white:#fff;
  --friend:#4867aa;
  --chirp:#3ea6e8;
  --orbit:#dd4b39;
}
*{box-sizing:border-box;margin:0;padding:0}
html,body{width:1200px;height:3383px;overflow:hidden}
body{font-family:"Lato",sans-serif;color:var(--body);background:var(--white);position:relative}
.section{position:absolute;left:0;width:1200px}
.abs{position:absolute}
.display{font-family:"Kalam",cursive;font-weight:700;white-space:nowrap}

/* header */
.site-header{top:0;height:90px;background:var(--white);border-top:2px solid var(--purple)}
.brand{left:100px;top:14px;height:62px;display:flex;align-items:center;gap:10px;font-family:"Kalam",cursive;font-weight:700;font-size:21px;color:var(--red);white-space:nowrap}
.brand-dot{width:18px;height:18px;border-radius:50%;background:var(--blue)}
.main-nav{left:366px;top:32px;display:flex;gap:29px;font-family:"Kalam",cursive;font-size:15px;color:var(--ink);align-items:center;white-space:nowrap}
.main-nav svg{display:block}

/* hero */
.hero{top:90px;height:542px;background:radial-gradient(ellipse at 45% 40%,#4a4a48 0%,#2a2a29 45%,#121212 100%)}
.hero-board{left:60px;top:140px;width:600px;height:330px;border-radius:40px;background:linear-gradient(150deg,#3a3a3a,#0f0f10 60%,#5a4a38)}
.hero-title{left:688px;top:196px;width:430px;text-align:center;font-size:42px;line-height:60px;color:var(--yellow)}

/* about */
.about{top:632px;height:638px;background:linear-gradient(180deg,#f2f2f0,#ecece9 60%,#f4f4f2)}
.about h2{left:129px;top:205px;font-size:40px;line-height:56px;color:var(--red);letter-spacing:1px}
.copy{font-size:14.5px;line-height:23px;color:var(--body)}
.about .copy{left:129px;top:270px;width:453px}
.copy p+p{margin-top:23px}
.detail-grid{left:636px;top:180px;width:466px;height:362px;display:grid;grid-template-columns:1fr 1fr;gap:6px;box-shadow:0 3px 10px rgba(0,0,0,.25)}
.detail-grid div{background:linear-gradient(145deg,#3b3b3b,#111)}
.detail-grid div:nth-child(2){background:linear-gradient(145deg,#ddd,#555 60%,#222)}
.detail-grid div:nth-child(4){background:linear-gradient(145deg,#f3f3f3,#222 55%,#2b8fc7)}

/* product */
.product{top:1270px;height:553px;background:linear-gradient(120deg,#2c2a28,#3c332e 40%,#4b2a28 70%,#2a2624)}
.product-shot{left:129px;top:50px;width:453px;height:455px;background:var(--white);padding:16px}
.product-shot .board{height:128px;margin-bottom:20px;border-radius:30px;background:linear-gradient(90deg,#2a2a2a,#666 50%,#2a2a2a)}
.product-shot .board:nth-child(2){background:linear-gradient(90deg,#222,#c8452c 45%,#e9a436 55%,#222)}
.product h2{left:616px;top:36px;font-size:36px;line-height:50px;color:var(--white)}
.price{left:616px;top:96px;font-family:"Poppins",sans-serif;font-weight:600;font-size:15px;color:var(--white)}
.price s{color:#bbb;margin-right:8px}
.qty{left:616px;top:153px;width:119px;height:32px;background:var(--white);font-size:14px;color:var(--ink);text-align:center;line-height:32px}
.add-cart{left:765px;top:153px;width:257px;height:32px;background:var(--red);color:var(--white);font-family:"Poppins",sans-serif;font-size:13px;font-weight:500;text-align:center;line-height:32px}
.product .copy{left:616px;top:212px;width:454px;color:#e6e6e6}
.share{top:467px;height:36px;border-radius:18px;color:var(--white);font-family:"Poppins",sans-serif;font-size:13px;font-weight:500;display:flex;align-items:center;justify-content:center;gap:6px}
.share i{width:10px;height:10px;border-radius:50%;background:var(--white);display:block}
.share.friend{left:616px;width:113px;background:var(--friend)}
.share.chirp{left:738px;width:112px;background:var(--chirp)}
.share.orbit{left:857px;width:113px;background:var(--orbit)}

/* testimonials */
.testimonials{top:1823px;height:297px;background:linear-gradient(100deg,#f6e9d2,#eaf2f4 30%,#f3dfe8 55%,#e3f0e6 80%,#f1e1ee)}
.testimonials h2{left:0;width:1200px;top:30px;text-align:center;font-size:36px;line-height:50px;color:var(--red)}
.quote{top:110px;width:266px;text-align:center;font-size:13px;line-height:24px;color:#444}
.quote .mark{font-family:"Kalam",cursive;font-weight:700;font-size:48px;line-height:34px;color:#333;display:block;margin-bottom:4px}
.quote.q1{left:153px}.quote.q2{left:466px}.quote.q3{left:778px}

/* photo band */
.photo-band{top:2120px;height:424px;display:flex}
.photo-band div{flex:1}
.photo-road{background:linear-gradient(180deg,#c9c5c4 0%,#9a7a66 35%,#d9d6d3 55%,#3a3a3c 100%)}
.photo-glow{background:radial-gradient(ellipse at 50% 75%,#8a3cff 0%,#3b2a63 30%,#2a2a2c 60%,#3a3a3c 100%)}

/* featured */
.featured{top:2544px;height:524px;background:linear-gradient(120deg,#f3e6cf,#e4eef1 35%,#f2dbe6 60%,#e6efe0 85%,#f0e4ee)}
.featured h2{left:0;width:1200px;top:68px;text-align:center;font-size:36px;line-height:50px;color:var(--red)}
.card{top:163px;width:214px}
.card .thumb{height:214px;background:var(--white);padding:18px;box-shadow:0 1px 4px rgba(0,0,0,.15)}
.card .thumb div{height:100%;background:linear-gradient(180deg,#eee,#ccc)}
.card.c1 .thumb div{background:linear-gradient(90deg,#fff 30%,#1a6fd0 40%,#8bd13c 50%,#1a6fd0 60%,#fff 70%)}
.card.c2 .thumb div{background:radial-gradient(ellipse at 50% 55%,#a11d1d,#3a1515 45%,#fff 70%)}
.card.c3 .thumb div{background:linear-gradient(90deg,#fff 40%,#222 48%,#222 52%,#fff 60%)}
.card.c4 .thumb div{background:radial-gradient(ellipse at 50% 55%,#bbb,#555 40%,#fff 70%)}
.card h3{margin-top:14px;font-size:19px;line-height:26px;color:var(--red);font-family:"Kalam",cursive;font-weight:700}
.card .cost{font-size:13px;color:var(--muted)}
.card.c1{left:135px}.card.c2{left:374px}.card.c3{left:614px}.card.c4{left:855px}

/* footer */
.site-footer{top:3068px;height:315px;background:linear-gradient(120deg,#1f2022,#2a2624 50%,#1e1f22);color:var(--white)}
.footer-links{left:133px;top:38px;list-style:none;font-family:"Poppins",sans-serif;font-size:13px;line-height:26px}
.mail-title{left:600px;top:40px;font-family:"Poppins",sans-serif;font-size:13px;letter-spacing:1px}
.mail-input{left:600px;top:72px;width:361px;height:37px;background:var(--white);color:var(--muted);font-size:14px;line-height:37px;padding-left:18px}
.mail-btn{left:961px;top:72px;width:102px;height:37px;background:var(--red);font-family:"Poppins",sans-serif;font-weight:600;font-size:12px;text-align:center;line-height:37px}
.socials{left:133px;top:194px;display:flex;gap:14px}
.socials span{width:18px;height:18px;background:var(--white);border-radius:3px;display:block}
.payments{left:887px;top:194px;display:flex;gap:8px}
.payments span{width:30px;height:19px;background:var(--white);border-radius:3px;display:block}
.copyright{left:133px;top:248px;font-family:"Poppins",sans-serif;font-size:12px}
</style>
</head>
<body>

<header class="section site-header">
  <a class="abs brand"><span class="brand-dot"></span>Tidewave Skateboards</a>
  <nav class="abs main-nav">
    <span>Home</span>
    <span>Electric Skateboards &#9662;</span>
    <span>Scooter</span>
    <span>Bikes</span>
    <span>Parts</span>
    <span>Apparel</span>
    <span>Blog</span>
    <span>Our Company</span>
    <svg width="14" height="14" viewBox="0 0 14 14" aria-label="Search"><circle cx="6" cy="6" r="4.5" fill="none" stroke="#222" stroke-width="2"/><line x1="9.5" y1="9.5" x2="13" y2="13" stroke="#222" stroke-width="2"/></svg>
    <svg width="14" height="14" viewBox="0 0 14 14" aria-label="Cart"><path d="M2 5h10l-1 8H3z" fill="#222"/><path d="M4.5 5V3.5a2.5 2.5 0 0 1 5 0V5" fill="none" stroke="#222" stroke-width="1.5"/></svg>
  </nav>
</header>

<section class="section hero">
  <div class="abs hero-board" role="img" aria-label="Off-road electric skateboard with large pneumatic wheels on dark asphalt"></div>
  <div class="abs hero-title display">TIDEWAVE SKATEBOARDS</div>
</section>

<section class="section about">
  <h2 class="abs display">ABOUT US</h2>
  <div class="abs copy">
    <p>Sed ut perspiciatis unde omnis iste natus error sit voluptatem accusantium doloremque laudantium, totam rem aperiam, eaque ipsa quae ab illo inventore veritatis et quasi architecto beatae vitae dicta sunt explicabo. Nemo enim ipsam voluptatem quia voluptas sit aspernatur.</p>
    <p>Sed ut perspiciatis unde omnis iste natus error sit voluptatem accusantium doloremque laudantium, totam rem aperiam, eaque ipsa quae ab illo inventore veritatis et quasi architecto beatae vitae dicta sunt explicabo. sequi nesciunt.</p>
  </div>
  <div class="abs detail-grid">
    <div role="img" aria-label="Close-up of skateboard motor and wiring"></div>
    <div role="img" aria-label="Close-up of an all-terrain wheel"></div>
    <div role="img" aria-label="Close-up of the battery enclosure"></div>
    <div role="img" aria-label="Close-up of a truck with blue mount"></div>
  </div>
</section>

<section class="section product">
  <div class="abs product-shot">
    <div class="board" role="img" aria-label="Skateboard deck top view"></div>
    <div class="board" role="img" aria-label="Skateboard underside with printed graphic"></div>
    <div class="board" role="img" aria-label="Skateboard three-quarter view"></div>
  </div>
  <h2 class="abs display">Our Product</h2>
  <div class="abs price"><s>$40.00</s>$35.00 Sale</div>
  <div class="abs qty">1</div>
  <div class="abs add-cart">ADD TO CART</div>
  <div class="abs copy">
    <p>Sed ut perspiciatis unde omnis iste natus error sit voluptatem accusantium doloremque laudantium, totam rem aperiam, eaque ipsa quae ab illo inventore veritatis et quasi architecto beatae vitae dicta sunt explicabo. Nemo enim ipsam voluptatem quia voluptas sit aspernatur.</p>
    <p>Sed ut perspiciatis unde omnis iste natus error sit voluptatem accusantium doloremque laudantium, totam rem aperiam, eaque ipsa quae ab illo inventore veritatis et quasi architecto beatae vitae dicta sunt explicabo. sequi nesciunt.</p>
  </div>
  <a class="abs share friend"><i></i>Friendwall</a>
  <a class="abs share chirp"><i></i>Chirper</a>
  <a class="abs share orbit"><i></i>Orbitplus</a>
</section>

<section class="section testimonials">
  <h2 class="abs display">Testimonials</h2>
  <blockquote class="abs quote q1"><span class="mark">&ldquo;</span>I was amazed at the quality of Kestrel. I wish I would have thought of it first. It is worth much more than I paid.<br>- Wadsworth H.</blockquote>
  <blockquote class="abs quote q2"><span class="mark">&ldquo;</span>I was amazed at the quality of Kestrel. I wish I would have thought of it first. It is worth much more than I paid.<br>- Ted T.</blockquote>
  <blockquote class="abs quote q3"><span class="mark">&ldquo;</span>I was amazed at the quality of Kestrel. I wish I would have thought of it first. It is worth much more than I paid.<br>- Roscoe J.</blockquote>
</section>

<section class="section photo-band">
  <div class="photo-road" role="img" aria-label="Rider skating down a desert highway with snowy mesas"></div>
  <div class="photo-glow" role="img" aria-label="Off-road electric skateboard lit with purple underglow on pavement"></div>
</section>

<section class="section featured">
  <h2 class="abs display">Featured Collection</h2>
  <article class="abs card c1"><div class="thumb"><div role="img" aria-label="Street electric skateboard with colourful deck"></div></div><h3>PRODUCT NAME</h3><p class="cost">$ 99.00</p></article>
  <article class="abs card c2"><div class="thumb"><div role="img" aria-label="Red electric chopper bike"></div></div><h3>PRODUCT NAME</h3><p class="cost">$ 99.00</p></article>
  <article class="abs card c3"><div class="thumb"><div role="img" aria-label="Black folding electric scooter"></div></div><h3>PRODUCT NAME</h3><p class="cost">$ 99.00</p></article>
  <article class="abs card c4"><div class="thumb"><div role="img" aria-label="Silver electric cruiser bike"></div></div><h3>PRODUCT NAME</h3><p class="cost">$ 99.00</p></article>
</section>

<footer class="section site-footer">
  <ul class="abs footer-links">
    <li>HOME</li><li>CATALOG</li><li>NEWS</li><li>CONTACT</li>
  </ul>
  <div class="abs mail-title">JOIN OUR MAILING LIST</div>
  <div class="abs mail-input">Email Address</div>
  <div class="abs mail-btn">SUBSCRIBE</div>
  <div class="abs socials"><span></span><span></span><span></span></div>
  <div class="abs payments"><span></span><span></span><span></span><span></span><span></span></div>
  <p class="abs copyright">Copyright &copy; 2018. Allrights Reserved.</p>
</footer>

</body>
</html>
```